Larkfield Clinic Booklet 2016

Larkfield Clinic is a multi-specialty Practice in Midtown Manhattan offering advanced care in multiple areas of medicine. See our table of contents (PDF Uploaded)
Our designed booklet should be clean, easy to read, contemporary, high-end and elegant.
We need a general theme, Layout for cover and templates for internal.
We are entertaining the idea of two different sizes
8 x 10
or
11 x 8.5
Our tagline " The Future of Medicine is Here"
We will provide all the text content
The link to our website
www.LarkfieldCL.example
Uploaded files are as follows.. Logo, Our Team Photo and the PDF listing the table of contents.

```html
<!DOCTYPE html>
<html lang="en">
<head>
<meta charset="utf-8">
<title>Larkfield Clinic Booklet – Stem Cell Therapy Spread</title>
<link rel="stylesheet" href="https://fonts.googleapis.com/css2?family=Open+Sans:wght@400;600;700&family=Jost:wght@400;500&display=swap">
<style>
  :root {
    --navy: #2b2b5e;
    --navy-deep: #242452;
    --gold: #c99a2e;
    --gold-light: #f0d257;
    --gold-dark: #a9780f;
    --text: #ffffff;
    --backdrop: #e4e4e6;
  }
  * { box-sizing: border-box; margin: 0; padding: 0; }
  html, body { width: 1200px; height: 800px; overflow: hidden; background: var(--backdrop); }
  .spread {
    position: absolute; left: 40px; top: 20px;
    width: 1120px; height: 760px;
    display: flex;
    box-shadow: 0 6px 24px rgba(0,0,0,.25);
  }
  .page {
    position: relative; width: 560px; height: 760px;
    background: var(--navy); color: var(--text);
    font-family: "Open Sans", sans-serif;
    overflow: hidden;
  }
  .page--left { border-right: 1px solid var(--navy-deep); }
  .hero-photo {
    position: absolute; left: 0; top: 0; width: 560px; height: 360px;
    background: linear-gradient(135deg, #dfe2e6 0%, #b8bdc4 45%, #8e96a0 75%, #5f6670 100%);
  }
  .title-tag {
    position: absolute; right: 0; top: 262px; width: 282px; height: 82px;
    background: var(--gold); padding: 16px 24px;
    font-family: "Jost", sans-serif; font-weight: 500; font-size: 19px; line-height: 1.25; color: #fff;
  }
  .columns {
    position: absolute; display: flex; gap: 22px;
  }
  .page--left .columns { left: 24px; top: 382px; width: 520px; }
  .page--right .columns { left: 24px; top: 24px; width: 516px; }
  .col { flex: 1; font-size: 10.4px; line-height: 1.36; text-align: justify; }
  .col p + p { margin-top: 14px; }
  .col h3 { font-size: 10.5px; font-weight: 700; margin: 14px 0 10px; }
  .site-url {
    position: absolute; bottom: 48px;
    font-family: "Jost", sans-serif; font-size: 12.5px; letter-spacing: .2px; color: #fff;
  }
  .page--left .site-url { right: 20px; }
  .page--right .site-url { left: 20px; }
  .gold-band {
    position: absolute; left: 0; bottom: 0; width: 100%; height: 34px;
    background: linear-gradient(90deg, var(--gold-dark), var(--gold-light) 45%, var(--gold) 70%, var(--gold-dark));
  }
  .folio {
    position: absolute; bottom: 9px; font-size: 12px; color: #fff; font-weight: 400;
  }
  .page--left .folio { left: 22px; }
  .page--right .folio { right: 22px; }
  .spine-image {
    position: absolute; left: 24px; top: 272px; width: 512px; height: 400px;
    border-radius: 12px;
    background: radial-gradient(ellipse at 50% 60%, #8a1a1a 0%, #3b2a2e 18%, #2a3438 40%, #1b2326 75%, #141a1c 100%);
  }
</style>
</head>
<body>
<main class="spread">
  <section class="page page--left">
    <div class="hero-photo" role="img" aria-label="Photo of two physicians performing a guided injection on a patient under an imaging arm"></div>
    <h2 class="title-tag">What is<br>Stem Cell Therapy?</h2>
    <div class="columns">
      <div class="col">
        <p>Regenerative medicine is an emerging branch of medicine with the goal of restoring organ and/or tissue function for patients with serious injuries or chronic disease in which the bodies own responses are not sufficient enough to restore functional tissue. A growing crisis in chronic pain in our active and aging population have driven a search for new and alternative therapies beyond pain killers and steroids. Something that can actually "fix" the problem once and for all, not just cover it up.</p>
        <p>New and current Regenerative Medicines can use stem cells to create living and functional tissues to regenerate and repair tissue and parts of the body that are damaged due to age, disease. Areas like arthritic knees of damaged spinal discs that are resistant to other treatments. Stem cells have the power to go to these damaged areas and regenerate new cells and tissues by performing a repair and</p>
      </div>
      <div class="col">
        <p>renewal process, restoring functionality. Regenerative medicine has the potential to provide a cure to problems that before required invasive surgeries or worse chronic pain medication. Stem cells can also be used to avoid future problems by repairing damaged tissue before the damage becomes so excessive that more invasive and risky treatments are needed. While some believe the therapeutic potential of stem cells has been overstated, an analysis of the potential benefits of stem cells based therapies indicates that 128 million people in the United States alone may benefit with the largest impact on patients with Cardiovascular disorders (5.5 million), autoimmune disorders (35 million) and diabetes (16 million US patients and more than 217 million worldwide): US patients with other disorders likely to benefit include osteoporosis (10 million), severe burns (0.3 million), spinal cord injuries (0.25 million).</p>
      </div>
    </div>
    <span class="site-url">www.LarkfieldCL.example</span>
    <div class="gold-band"></div>
    <span class="folio">01</span>
  </section>

  <section class="page page--right">
    <div class="columns">
      <div class="col">
        <p>Our office has been on the forefront of stem cell injection treatments as one of the earliest adopters. Our team of hematologists, sports medicine and orthopedic specialists have been able to give patients relief who have otherwise been disabled due to pain. While this is by no means a miracle it does hold promise to be the breakthrough that we have all been waiting for.</p>
        <h3>Where do the stem cells come from?</h3>
        <p>This is a far more complex question. There are many types of stem cells, many of which hold great promise for tomorrow, and others that are being used today. The main dividing line is between Adult Stem Cells (ASC) and Embryonic Stem Cells (ESC). ESC's have captured the attention of early stem cell researchers because</p>
      </div>
      <div class="col">
        <p>of their inherent ability to expand into any type (tissue, bone, etc). While promising, research shows that ESC's present a high risk of tumor formation because of their ability to reproduce without end. There is also little evidence that shows that ESC's are ready for use in the treatment of diseases in humans. Adult stem cells, on the other hand, are the repair cells that our bodies currently use to mend wounds and heal ourselves. Unlike ESC's, adult stem cells have been shown to be effective in animal and early human clinical models for treating a wide variety of diseases, including orthopedics and neurologic diseases. Additionally, ASC's can be safely collected from various sources in the human body, such as fat, peripheral blood and bone marrow.</p>
      </div>
    </div>
    <div class="spine-image" role="img" aria-label="X-ray style image of a human back with the lower spine highlighted in red"></div>
    <span class="site-url">www.LarkfieldCL.example</span>
    <div class="gold-band"></div>
    <span class="folio">02</span>
  </section>
</main>
</body>
</html>
```